Lantern Advisory Business Cards

We need a new layout for our business cards. We have a logo already. But we might be interested in only using the Lantern portion of the logo. It has been uploaded.

We would like cards that are not overly busy. Clean. Modern. Perhaps a gray color for one side.

On the back, we would like to have the lantern part of the logo and "Take the Leap, we've got you!"

Our business provides medics and safety training for corporate clients. Our website is www.lanternadvisoryllc.example.

Industry/Entity Type

Business

Contact Information for Business Card

We want include name, email address, cell phone, main line number, and website URL on the front. Use the following as an example: Marla Tobin, marla@lanternadvisoryllc.example, 402.318.7264 (cell), 402.947.315, and www.lanternadvisoryllc.example.

Font styles to use
Serif
Sans Serif

Requirements
Must have
• All required information. Back side logo with "Step forward, we will light the way!"
Nice to have
• If possible, we would like to consider creating a card in a non-standard shape. Perhaps, the shape of a lantern. Just interested in understanding the option.

```html
<!DOCTYPE html>
<html lang="en">
<head>
<meta charset="utf-8">
<title>Lantern Advisory Business Cards</title>
<link rel="stylesheet" href="https://fonts.googleapis.com/css2?family=Cinzel:wght@500&family=Open+Sans:ital,wght@0,400;0,600;1,400&display=swap">
<style>
  :root {
    --blue: #0d5fb3;
    --blue-light: #1b78cc;
    --ink: #2b2b2b;
    --muted: #555555;
    --card: #ffffff;
    --card-shade: #e9eaec;
    --canvas: #d9d6d1;
  }
  * { box-sizing: border-box; margin: 0; padding: 0; }
  html, body { width: 1200px; height: 1023px; overflow: hidden; }
  body {
    background: var(--canvas);
    font-family: "Open Sans", sans-serif;
    position: relative;
  }
  .card {
    position: absolute;
    left: 250px;
    width: 700px;
    height: 400px;
    border-radius: 22px;
    background: linear-gradient(160deg, var(--card) 45%, var(--card-shade) 100%);
    box-shadow: 0 6px 18px rgba(0,0,0,.18);
    overflow: hidden;
  }
  .card--front { top: 70px; }
  .card--back { top: 553px; }

  /* Front */
  .front-brand {
    position: absolute;
    left: 60px;
    top: 118px;
    display: flex;
    align-items: center;
    gap: 14px;
  }
  .brand-mark {
    width: 22px; height: 22px;
    border-radius: 50%;
    background: var(--blue);
  }
  .brand-name {
    font-family: "Cinzel", serif;
    font-weight: 500;
    font-size: 34px;
    color: var(--ink);
    letter-spacing: 1px;
    line-height: 1;
  }
  .brand-tagline {
    font-family: "Open Sans", sans-serif;
    font-size: 9px;
    letter-spacing: 5px;
    color: var(--muted);
    text-transform: uppercase;
  }
  .front-tagline { position: absolute; left: 96px; top: 160px; }
  .front-band {
    position: absolute;
    top: 218px;
    height: 40px;
    background: linear-gradient(90deg, var(--blue), var(--blue-light));
  }
  .front-band--lead { left: 0; width: 48px; }
  .front-band--main { left: 250px; right: 0; }
  .person-name {
    position: absolute;
    left: 58px;
    top: 216px;
    font-size: 30px;
    color: var(--blue);
    line-height: 40px;
  }
  .contact-list {
    position: absolute;
    right: 40px;
    top: 282px;
    list-style: none;
    text-align: right;
    font-size: 14px;
    line-height: 22px;
    color: var(--ink);
  }
  .contact-list li { display: flex; justify-content: flex-end; align-items: center; gap: 8px; }
  .contact-list svg { width: 12px; height: 12px; fill: none; stroke: var(--blue); stroke-width: 1.6; }

  /* Back */
  .back-mark {
    position: absolute;
    right: 130px;
    top: 52px;
    width: 80px; height: 80px;
    border-radius: 50%;
    background: var(--blue);
  }
  .back-band {
    position: absolute;
    left: 0; right: 0;
    top: 160px;
    height: 92px;
    background: linear-gradient(90deg, var(--blue), var(--blue-light));
    color: #fff;
    padding: 16px 0 0 70px;
  }
  .back-band .brand-name { color: #fff; font-size: 40px; }
  .back-band .brand-tagline { color: #fff; margin: 10px 0 0 4px; letter-spacing: 9px; font-size: 10px; }
  .back-slogan {
    position: absolute;
    left: 70px;
    top: 284px;
    font-size: 22px;
    color: var(--blue);
    letter-spacing: .5px;
  }
</style>
</head>
<body>
  <section class="card card--front" aria-label="Business card front">
    <div class="front-brand">
      <span class="brand-mark"></span>
      <span class="brand-name">Lantern Advisory</span>
    </div>
    <p class="brand-tagline front-tagline">The Readiness Partners</p>
    <div class="front-band front-band--lead"></div>
    <p class="person-name">Marla Tobin</p>
    <div class="front-band front-band--main"></div>
    <ul class="contact-list">
      <li>402.318.7264
        <svg viewBox="0 0 12 12"><path d="M3 1 L5 3 L4 5 Q6 8 8 8 L9 7 L11 9 L9 11 Q2 10 1 3 Z"/></svg></li>
      <li>402.947.315
        <svg viewBox="0 0 12 12"><rect x="3" y="1" width="6" height="10" rx="1"/></svg></li>
      <li>marla@lanternadvisoryllc.example
        <svg viewBox="0 0 12 12"><rect x="1" y="3" width="10" height="7"/><path d="M1 3 L6 7 L11 3"/></svg></li>
      <li>www.lanternadvisoryllc.example
        <svg viewBox="0 0 12 12"><circle cx="6" cy="6" r="5"/><path d="M1 6 H11 M6 1 Q3 6 6 11 Q9 6 6 1"/></svg></li>
    </ul>
  </section>

  <section class="card card--back" aria-label="Business card back">
    <span class="back-mark"></span>
    <div class="back-band">
      <p class="brand-name">Lantern Advisory</p>
      <p class="brand-tagline">The Readiness Partners</p>
    </div>
    <p class="back-slogan">Step forward, we will light the way!</p>
  </section>
</body>
</html>
```